Business Card Design

We need a business card design for a new dental practice in Brisbane. I'd like the basic details and logo on one side and appointment schedule on the other side. It is based in CBD office area and would prefer a professional and modern design.
Target Market(s)
20-60 years old office workers and residents with high education levels
Industry/Entity Type
Dental
Contact Information for Business Card
Harbourlight Dental
Dr Marcus Lindqvist
Principal Dentist
07 3194 6627
admin@harbourlightdentistry.example.au
www.harbourlightdentistry.example.au
S27, Level 3, Ferndale North Tower, 318 Gorrick St, Alderwood Heights, QLD 4118

```html
<!DOCTYPE html>
<html lang="en">
<head>
<meta charset="utf-8">
<title>Harbourlight Dental – Business Card</title>
<link href="https://fonts.googleapis.com/css2?family=Open+Sans:wght@400;600&display=swap" rel="stylesheet">
<style>
  :root {
    --bg: #e9ebee;
    --navy: #0c1a33;
    --navy-deep: #07111f;
    --navy-soft: #16284a;
    --sky: #5aaee0;
    --azure: #1e8fd6;
    --ink: #1b1f26;
    --paper: #ffffff;
    --field: #ffffff;
    --muted: #6f7782;
  }
  * { box-sizing: border-box; margin: 0; padding: 0; }
  html, body {
    width: 1200px; height: 784px; overflow: hidden;
    background: var(--bg);
    font-family: "Open Sans", Arial, sans-serif;
  }
  .canvas {
    position: relative; width: 1200px; height: 784px;
    display: flex; align-items: center; justify-content: center; gap: 40px;
  }
  .card {
    position: relative; width: 540px; height: 310px;
    border-radius: 4px; overflow: hidden;
    box-shadow: 0 10px 28px rgba(10, 20, 40, .18);
  }

  /* Appointment side */
  .card--appointment {
    background: radial-gradient(ellipse at 40% 30%, var(--navy-soft) 0%, var(--navy) 55%, var(--navy-deep) 100%);
    color: var(--sky);
  }
  .appointment__title {
    position: absolute; top: 34px; left: 0; width: 100%;
    text-align: center; font-size: 17px; letter-spacing: .3px;
  }
  .appointment__label {
    position: absolute; font-size: 15px; letter-spacing: .3px;
  }
  .appointment__field {
    position: absolute; height: 26px; background: var(--field);
    box-shadow: inset 0 2px 3px rgba(0,0,0,.35);
  }
  .label-name { left: 34px; top: 96px; }
  .field-name { left: 96px; top: 92px; width: 410px; }
  .label-time { left: 306px; top: 146px; }
  .field-time { left: 360px; top: 142px; width: 146px; }
  .label-date { left: 34px; top: 196px; }
  .field-date { left: 96px; top: 192px; width: 190px; }
  .brand--appointment {
    position: absolute; right: 30px; bottom: 30px;
    display: flex; align-items: center; gap: 8px;
    color: var(--sky); font-size: 15px; font-weight: 600;
  }
  .brand__dot {
    width: 14px; height: 14px; border-radius: 50%; background: var(--sky);
  }

  /* Contact side */
  .card--contact { background: var(--paper); color: var(--ink); }
  .dentist {
    position: absolute; top: 24px; right: 30px; text-align: right;
  }
  .dentist__name { font-size: 15px; color: var(--ink); }
  .dentist__role { font-size: 10px; color: var(--azure); margin-top: 1px; }
  .brand--contact {
    position: absolute; left: 40px; top: 92px;
    display: flex; align-items: center; gap: 12px;
    color: var(--ink); font-size: 30px; font-weight: 400; letter-spacing: .2px;
  }
  .brand--contact .brand__dot { width: 26px; height: 26px; background: var(--azure); }
  .contact-list {
    position: absolute; left: 40px; top: 170px; list-style: none;
    font-size: 13px; line-height: 17px; color: var(--ink);
  }
  .contact-list li { display: flex; align-items: flex-start; gap: 8px; }
  .contact-list svg { width: 13px; height: 13px; margin-top: 2px; flex: none; fill: var(--azure); }
  .contact-band {
    position: absolute; left: 0; bottom: 0; width: 100%; height: 24px;
    background: var(--navy); border-top: 4px solid var(--azure);
  }
</style>
</head>
<body>
<main class="canvas">

  <section class="card card--appointment" aria-label="Appointment side">
    <h2 class="appointment__title" style="font-weight:400">Appointment</h2>
    <span class="appointment__label label-name">Name:</span>
    <span class="appointment__field field-name"></span>
    <span class="appointment__label label-time">Time :</span>
    <span class="appointment__field field-time"></span>
    <span class="appointment__label label-date">Date :</span>
    <span class="appointment__field field-date"></span>
    <div class="brand brand--appointment">
      <span class="brand__dot"></span>
      <span>Harbourlight Dental</span>
    </div>
  </section>

  <section class="card card--contact" aria-label="Contact side">
    <div class="dentist">
      <div class="dentist__name">Dr Marcus Lindqvist</div>
      <div class="dentist__role">Principal Dentist</div>
    </div>
    <div class="brand brand--contact">
      <span class="brand__dot"></span>
      <span>Harbourlight Dental</span>
    </div>
    <ul class="contact-list">
      <li>
        <svg viewBox="0 0 24 24" aria-hidden="true"><path d="M6.6 10.8a15.2 15.2 0 0 0 6.6 6.6l2.2-2.2c.3-.3.7-.4 1-.2 1.1.4 2.3.6 3.6.6.6 0 1 .4 1 1V20c0 .6-.4 1-1 1A17 17 0 0 1 3 4c0-.6.4-1 1-1h3.5c.6 0 1 .4 1 1 0 1.3.2 2.5.6 3.6.1.3 0 .7-.2 1z"/></svg>
        <span>07 3194 6627</span>
      </li>
      <li>
        <svg viewBox="0 0 24 24" aria-hidden="true"><path d="M3 5h18v14H3z M3 5l9 7 9-7" fill="none" stroke="#1e8fd6" stroke-width="2"/></svg>
        <span>admin@harbourlightdentistry.example.au</span>
      </li>
      <li>
        <svg viewBox="0 0 24 24" aria-hidden="true"><g fill="none" stroke="#1e8fd6" stroke-width="2"><circle cx="12" cy="12" r="9"/><ellipse cx="12" cy="12" rx="4" ry="9"/><path d="M3 12h18"/></g></svg>
        <span>www.harbourlightdentistry.example.au</span>
      </li>
      <li>
        <svg viewBox="0 0 24 24" aria-hidden="true"><path d="M12 3 2 12h3v9h5v-6h4v6h5v-9h3z"/></svg>
        <span>S27, Level 3, Ferndale North Tower,<br>318 Gorrick St, Alderwood Heights, QLD 4118</span>
      </li>
    </ul>
    <div class="contact-band"></div>
  </section>

</main>
</body>
</html>
```